Sun Keel (www.sunkeel.com) web site development

Sun Keel is a new Fishing, Spearfishing Charter operator offering private charters in North Belize, Turneffe, Lighthouse Reef and the Blue Hole. The logo of the company has been designed by Pixelvane, some months ago. We have also developed a small brochure which can be the base for the website development (at least colors, fonts, etc.).
Pictures and Video should be an important asset of this website. We need to be able to update contents (video, photos), update prices and destinations, etc.

Target Market(s)

High hand, fishing and spearfishing enthusiasts.

Industry/Entity Type

Yacht charter

Coding

Coded - Design and coding required

Number of Pages Required

4 page

Colors
EB3D1F
EC4F4E
F09395
F8D3D4
FCEDEE

Requirements
Must have
• Optimized for phone and tablet navigation, must be easy to update with photos and video, connected to our Instagram and Facebook page,

```html
<!DOCTYPE html>
<html lang="en">
<head>
<meta charset="utf-8">
<title>Sun Keel – Fishing, Spearfishing &amp; Snorkeling Private Charters</title>
<link href="https://fonts.googleapis.com/css2?family=Exo+2:ital,wght@0,700;1,600;1,700;1,800&family=Arimo:wght@400&family=Jost:wght@400&display=swap" rel="stylesheet">
<style>
:root{
  --red:#e2001a;
  --teal:#1f3a45;
  --teal-dark:#1b333d;
  --ink:#2b2b2b;
  --muted:#4a4a4a;
  --white:#ffffff;
}
*{margin:0;padding:0;box-sizing:border-box}
html,body{width:1200px;height:3811px;overflow:hidden;background:var(--white)}
body{position:relative;font-family:"Arimo",Arial,sans-serif;color:var(--ink)}
.head{font-family:"Exo 2",sans-serif;font-style:italic;font-weight:700}
section,header,footer{position:absolute;left:0;width:1200px}
.btn{position:absolute;display:flex;align-items:center;justify-content:center;gap:8px;background:var(--red);color:var(--white);border-radius:40px;font-family:"Exo 2",sans-serif;font-style:italic;font-weight:700}

/* header */
.site-header{top:0;height:164px}
.brand{position:absolute;left:111px;top:78px;display:flex;align-items:center;gap:12px}
.brand-dot{width:26px;height:26px;border-radius:50%;background:var(--red)}
.brand-name{font-family:"Exo 2",sans-serif;font-weight:700;font-size:46px;color:var(--teal);line-height:1}
.call{position:absolute;left:830px;top:21px;display:flex;align-items:center;gap:12px}
.call-icon{width:63px;height:63px;border-radius:50%;background:var(--red);display:flex;align-items:center;justify-content:center}
.call-text{font-size:17px;color:var(--red)}
.nav{position:absolute;top:114px;left:0;width:1200px;font-size:15px;color:var(--ink)}
.nav a{position:absolute;text-decoration:none;color:inherit}
.nav a.active{color:var(--red)}

/* hero */
.hero{top:164px;height:776px;overflow:hidden}
.hero-photo{position:absolute;inset:0;background:
  radial-gradient(ellipse 420px 300px at 850px 420px,#b58a55 0%,rgba(181,138,85,0) 70%),
  radial-gradient(ellipse 300px 200px at 520px 120px,#c79a7c 0%,rgba(199,154,124,0) 70%),
  linear-gradient(100deg,#3c2a22 0%,#5a4538 30%,#8d7464 55%,#c8b4a4 78%,#e3d3c6 100%)}
.hero-shade{position:absolute;inset:0;background:linear-gradient(90deg,rgba(0,0,0,.45) 0%,rgba(0,0,0,0) 55%)}
.hero-title{position:absolute;left:111px;top:400px;font-size:108px;font-weight:800;color:var(--white);line-height:1}
.hero-sub{position:absolute;left:111px;top:526px;font-size:21px;color:var(--white)}
.hero .btn{left:111px;top:580px;width:166px;height:58px;font-size:18px}
.hero-wave{position:absolute;left:0;top:0}

/* welcome */
.welcome{top:940px;height:420px;text-align:center}
.section-title{font-size:40px;color:var(--teal)}
.section-title span{color:var(--red)}
.welcome .section-title{position:absolute;top:56px;width:100%}
.rule{position:absolute;width:52px;height:3px;background:var(--teal)}
.welcome .rule{left:574px;top:118px}
.welcome p{position:absolute;left:271px;top:140px;width:658px;font-size:14px;line-height:26px;color:var(--muted)}
.welcome .btn{left:511px;top:300px;width:177px;height:56px;font-size:19px}

/* charters */
.charters{top:1360px;height:465px}
.card{position:absolute;top:0;width:312px;height:465px;color:var(--white);text-align:center}
.card-photo{height:252px}
.card-body{height:213px;background:var(--teal);padding-top:32px}
.card.featured .card-body{background:var(--red)}
.card h3{font-size:17px}
.card .price{font-size:22px;margin-top:10px}
.card p{font-size:13.5px;line-height:26px;margin:14px auto 0;width:260px}

/* band */
.promise{top:1903px;height:568px;overflow:hidden}
.promise-photo{position:absolute;inset:0;background:
  radial-gradient(ellipse 260px 200px at 380px 300px,#5b5854 0%,rgba(91,88,84,0) 70%),
  linear-gradient(90deg,#1f1c1b 0%,#3a3430 30%,#6e5a4d 55%,#8a6d56 75%,#5e4a3d 100%)}
.promise-title{position:absolute;left:642px;top:146px;font-size:58px;color:var(--white);line-height:1}
.promise-sub{position:absolute;left:642px;top:216px;font-size:38px;color:var(--white);line-height:1}
.promise p{position:absolute;left:642px;top:278px;width:440px;font-size:13.5px;line-height:26px;color:var(--white)}
.promise .btn{left:641px;top:380px;width:155px;height:52px;font-size:18px}

/* video */
.video{top:2471px;height:528px}
.video-photo{position:absolute;left:111px;top:77px;width:506px;height:374px;background:linear-gradient(180deg,#cfe6f1 0%,#4aa3cf 18%,#1e78b3 45%,#145f93 75%,#0f4a73 100%)}
.video .section-title{position:absolute;left:664px;top:100px}
.video .rule{left:667px;top:161px}
.video p{position:absolute;left:667px;top:196px;width:406px;font-size:13.5px;line-height:26px;color:var(--muted);text-align:justify}
.video .btn{left:669px;top:367px;width:163px;height:51px;font-size:17px}

/* testimonials */
.clients{top:2999px;height:421px;background:var(--red);color:var(--white)}
.client-photo{position:absolute;left:171px;top:72px;width:258px;height:258px;border-radius:50%;background:radial-gradient(circle at 50% 40%,#9fc6dd 0%,#6f9cb3 45%,#3e5f4e 80%,#2e4838 100%)}
.quote-badge{position:absolute;left:274px;top:308px;width:56px;height:56px;border-radius:50%;background:var(--teal);display:flex;align-items:center;justify-content:center}
.clients h2{position:absolute;left:485px;top:86px;font-size:34px}
.clients p{position:absolute;left:485px;top:152px;width:579px;font-size:14px;line-height:27px;text-align:justify}
.client-name{position:absolute;left:485px;top:303px;font-size:14px}
.client-name b{font-family:"Exo 2",sans-serif;font-style:italic;font-weight:700;font-size:23px}
.arrow{position:absolute;top:166px}

/* footer */
.site-footer{top:3420px;height:391px;background:var(--teal-dark);color:var(--white)}
.foot-brand{position:absolute;left:148px;top:110px;display:flex;align-items:center;gap:12px}
.foot-brand .brand-name{color:var(--white);font-size:48px}
.socials{position:absolute;left:178px;top:248px;display:flex;gap:7px}
.socials span{width:36px;height:36px;border-radius:50%;border:2px solid var(--white)}
.foot-col{position:absolute;top:62px}
.foot-col h4{font-family:"Exo 2",sans-serif;font-style:italic;font-weight:700;font-size:22px;margin-bottom:22px}
.links li{list-style:none;font-size:14px;line-height:30px;display:flex;align-items:center;gap:16px}
.contact-lines div{font-size:14px;line-height:29px}
.newsletter p{font-size:12.5px;line-height:22px;width:230px}
.email{margin-top:18px;width:226px;height:41px;background:var(--white);border-radius:3px;color:#333;font-size:11px;padding:14px 0 0 14px}
.submit{margin-top:11px;width:99px;height:34px;background:var(--red);border-radius:2px;font-size:13px;text-align:center;line-height:34px}
.copy{position:absolute;top:340px;width:100%;text-align:center;font-family:"Jost",sans-serif;font-size:15px}
</style>
</head>
<body>

<header class="site-header">
  <div class="brand"><span class="brand-dot"></span><span class="brand-name">Sun Keel</span></div>
  <div class="call">
    <div class="call-icon">
      <svg width="22" height="22" viewBox="0 0 24 24"><path fill="#fff" d="M6.6 10.8a15.1 15.1 0 0 0 6.6 6.6l2.2-2.2c.3-.3.7-.4 1-.2 1.1.4 2.3.6 3.6.6.6 0 1 .4 1 1V20c0 .6-.4 1-1 1A17 17 0 0 1 3 4c0-.6.4-1 1-1h3.5c.6 0 1 .4 1 1 0 1.3.2 2.5.6 3.6.1.3 0 .7-.2 1z"/></svg>
    </div>
    <span class="call-text head">CALL US : 000-555-0147</span>
  </div>
  <nav class="nav head">
    <a class="active" style="left:478px">HOME</a>
    <a style="left:562px">ABOUT US</a>
    <a style="left:673px">SERVICES</a>
    <a style="left:781px">TESTIMONIALS</a>
    <a style="left:923px">NEWS</a>
    <a style="left:1006px">CONTACT US</a>
  </nav>
</header>

<section class="hero">
  <div class="hero-photo" role="img" aria-label="Angler on a boat holding up a freshly caught fish with his rod"></div>
  <div class="hero-shade"></div>
  <h1 class="hero-title head">Sun Keel</h1>
  <div class="hero-sub head">Fishing, Spearfishing &amp; Snorkeling Private Charters</div>
  <div class="btn">READ MORE</div>
  <svg class="hero-wave" width="1200" height="776" viewBox="0 0 1200 776">
    <path d="M0 718 C120 760 230 786 420 752 C640 712 860 640 1040 644 C1120 646 1170 664 1200 690 L1200 776 L0 776 Z" fill="#fff"/>
    <path d="M0 704 C120 752 230 778 420 742 C640 702 860 630 1040 632 C1120 634 1170 650 1200 674 L1200 690 C1170 664 1120 646 1040 644 C860 640 640 712 420 752 C230 786 120 760 0 718 Z" fill="#e2001a"/>
  </svg>
</section>

<section class="welcome">
  <h2 class="section-title head">Welcome To <span>Sun Keel</span></h2>
  <div class="rule"></div>
  <p>Sed ut perspiciatis unde omnis iste natus error sit voluptatem accusantium doloremque laudantium, totam rem aperiam, eaque ipsa quae ab illo inventore veritatis et quasi architecto beatae vitae dicta sunt explicabo. Nemo enim ipsam voluptatem quia voluptas sit aspernatur aut odit aut fugit, sed quia consequuntur magni dolores eos qui ratione voluptatem sequi nesciunt. Neque porro quisquam est, qui dolorem ipsum quia dolor incidunt ut labore et dolore magnam aliquam quaerat voluptatem.</p>
  <div class="btn">Read More</div>
</section>

<section class="charters">
  <article class="card" style="left:111px">
    <div class="card-photo" role="img" aria-label="Angler on an offshore boat holding a large tuna" style="background:linear-gradient(180deg,#6d93c9 0%,#a7c0df 30%,#2f5a86 55%,#7a7f84 100%)"></div>
    <div class="card-body">
      <h3 class="head">FISHING PRIVATE CHARTERS</h3>
      <div class="price head">US$ 1.000</div>
      <p>Our Fishing Charters are all Offshore trips Depending on your choice we can offer a variety of fishing options.</p>
    </div>
  </article>
  <article class="card featured" style="left:444px">
    <div class="card-photo" role="img" aria-label="Spearfisher underwater beside a large fish" style="background:linear-gradient(180deg,#1f86c4 0%,#2a92c8 50%,#1a6da3 100%)"></div>
    <div class="card-body">
      <h3 class="head">SPEARFISHING PRIVATE CHARTERS</h3>
      <div class="price head">US$ 1.400</div>
      <p>We welcome all experience levels and you will be accompaniedby a safe diver in the water at all times to help</p>
    </div>
  </article>
  <article class="card" style="left:777px">
    <div class="card-photo" role="img" aria-label="Group of snorkelers swimming among a school of fish" style="background:linear-gradient(180deg,#7fb1d8 0%,#3f97c6 45%,#2b86a9 100%)"></div>
    <div class="card-body">
      <h3 class="head">SNORKELLING PRIVATE CHARTERS</h3>
      <div class="price head">US$ 1.200</div>
      <p>We offer snorkelling trips to the Hole Chan Marine Reserve, to Shark Ray Alley, Coral Gardens, all destinations inside</p>
    </div>
  </article>
</section>

<section class="promise">
  <div class="promise-photo" role="img" aria-label="Close-up of hands holding a fishing rod and spinning reel at dusk"></div>
  <h2 class="promise-title head">SUN KEEL</h2>
  <h3 class="promise-sub head">BIG FISH IS WHAT WE DO</h3>
  <p>Sun Keel offers Fishing , Spearfishing and Snorkeling private charters in North Belize, Turneffe, Lighthouse Reef and the Blue Hole. No need to your privacy and let us pamper you with our exclusive service.</p>
  <div class="btn">Read More</div>
</section>

<section class="video">
  <div class="video-photo" role="img" aria-label="Young snorkeler swimming underwater among striped reef fish"></div>
  <h2 class="section-title head">Our <span>Video</span></h2>
  <div class="rule"></div>
  <p>We welcome both experienced fishermen/free divers and beginners. You can learn from our guides and even attend one of our introd uctory class to free dive and spearfishing from professional licensed instructors and expert scuba divers. You are welcome to take your gear with you, or leave us to provide you with all you need for an unforgettable experience.</p>
  <div class="btn">PLAY VIDEO
    <svg width="15" height="15" viewBox="0 0 16 16"><circle cx="8" cy="8" r="6.5" fill="none" stroke="#fff" stroke-width="2"/><path d="M6.5 5v6l4.5-3z" fill="#fff"/></svg>
  </div>
</section>

<section class="clients">
  <svg class="arrow" style="left:57px" width="26" height="92" viewBox="0 0 26 92"><path d="M24 2 L2 46 L24 90" fill="none" stroke="#fff" stroke-width="1.5" opacity=".8"/></svg>
  <svg class="arrow" style="left:1112px" width="26" height="92" viewBox="0 0 26 92"><path d="M2 2 L24 46 L2 90" fill="none" stroke="#fff" stroke-width="1.5" opacity=".8"/></svg>
  <div class="client-photo" role="img" aria-label="Two happy anglers on a boat holding a large catch"></div>
  <div class="quote-badge">
    <svg width="22" height="18" viewBox="0 0 22 18"><path d="M1 1h8v8c0 4-2 7-6 8l-1-2c2-1 3-3 3-5H1z M13 1h8v8c0 4-2 7-6 8l-1-2c2-1 3-3 3-5h-4z" fill="#fff"/></svg>
  </div>
  <h2 class="head">What Our Clients Say</h2>
  <p>Sed ut perspiciatis unde omnis iste natus error sit voluptatem accusantium doloremque laudantium, totam rem aperiam, eaque ipsa quae ab illo inventore veritatis et quasi architecto beatae vitae dicta sunt explicabo. Nemo enim ipsam voluptatem quia voluptas sit aspernatur aut odit aut fugit, sed quia consequuntur magni dolores eos qui ratione labore et dolore magnam omnis iste natus error sit aliquam quaerat voluptatem.</p>
  <div class="client-name"><b>Mara Quill,</b> Sed ut perspiciatis unde</div>
</section>

<footer class="site-footer">
  <div class="foot-brand"><span class="brand-dot"></span><span class="brand-name">Sun Keel</span></div>
  <div class="socials"><span></span><span></span><span></span><span></span><span></span></div>

  <div class="foot-col links" style="left:431px">
    <h4>LINKS</h4>
    <ul>
      <li><svg width="10" height="10" viewBox="0 0 10 10"><path d="M1 1l4 4-4 4M5 1l4 4-4 4" fill="none" stroke="#fff" stroke-width="1.4"/></svg>HOME</li>
      <li><svg width="10" height="10" viewBox="0 0 10 10"><path d="M1 1l4 4-4 4M5 1l4 4-4 4" fill="none" stroke="#fff" stroke-width="1.4"/></svg>ABOUT US</li>
      <li><svg width="10" height="10" viewBox="0 0 10 10"><path d="M1 1l4 4-4 4M5 1l4 4-4 4" fill="none" stroke="#fff" stroke-width="1.4"/></svg>SERVICES</li>
      <li><svg width="10" height="10" viewBox="0 0 10 10"><path d="M1 1l4 4-4 4M5 1l4 4-4 4" fill="none" stroke="#fff" stroke-width="1.4"/></svg>TESTIMONIALS</li>
      <li><svg width="10" height="10" viewBox="0 0 10 10"><path d="M1 1l4 4-4 4M5 1l4 4-4 4" fill="none" stroke="#fff" stroke-width="1.4"/></svg>NEWS</li>
      <li><svg width="10" height="10" viewBox="0 0 10 10"><path d="M1 1l4 4-4 4M5 1l4 4-4 4" fill="none" stroke="#fff" stroke-width="1.4"/></svg>CONTACT US</li>
    </ul>
  </div>

  <div class="foot-col contact-lines" style="left:616px">
    <h4>GET IN TOUCH</h4>
    <div>Tele : 000-555-0147</div>
    <div>Fax : 000-555-0148</div>
    <div>hello@sunkeel.com</div>
    <div>214 Marina Row Lorem Ipsum</div>
    <div>Dummy Text 40218</div>
  </div>

  <div class="foot-col newsletter" style="left:862px">
    <h4>NEWSLETTER</h4>
    <p>Sed ut perspiciatis unde error sit vol uptatem accusantium...</p>
    <div class="email">Enter Email Id :</div>
    <div class="submit">Submit</div>
  </div>

  <div class="copy">© Copyright 2021 Sun Keel.All Rights Reserved</div>
</footer>

</body>
</html>
```